Scandinavian Style Label for Vitamin (B-Complex) Bottle, 500mg

The Brand name is: Sun to Sun- Slogan Rise Brighter!
The bottle will be brown see-through plastic, cap also plastic(same color).
Label color should be in lighter shades, also would like to add the color gold. Brand name will be in gold as well.
Want it to be tasty and eye-catching. Could use contrasting colors that are visible from far.
Should have Supports Energy Metabolism, and Supports Heart Health written on them. Also needs Lactose and Gluten Free, Good Manufacturing signs.
Will include 60 coated caplets.
Label width is 180mm and height 70mm.
Label nutritional facts attached as a file.
Will be in English

Target Market(s)

Scandinavia, Russia

Industry/Entity Type

Vitamin

Font styles to use
Serif
Sans Serif
Script

Colors

Designer to choose colors to be used in the design.

Requirements
Must have
• Tasty touch of gold, elegance
Nice to have
• Vectors, dots, lines, drops
Should not have
• No dark colors and not too many colors

```html
<!DOCTYPE html>
<html lang="en">
<head>
<meta charset="utf-8">
<title>Sun to Sun Vitamins – B-Complex Label</title>
<link rel="stylesheet" href="https://fonts.googleapis.com/css2?family=Questrial&family=Cinzel:wght@700&family=Oswald:wght@600&family=Roboto:wght@700&family=Great+Vibes&display=swap">
<style>
  :root {
    --page: #ffffff;
    --frame: #333333;
    --label-top: #fbf7ee;
    --label-body: #f4ecdc;
    --label-bottom: #ece1c9;
    --band-light: #efe2c4;
    --gold: #d9a94a;
    --gold-light: #f6dd97;
    --gold-dark: #a7782a;
    --gold-text: #b8872f;
    --silver: #f2f2f2;
    --silver-dark: #bdbdbd;
    --cream: #fffaf0;
    --ink: #3b2e1c;
  }
  * { box-sizing: border-box; margin: 0; padding: 0; }
  html, body { width: 1200px; height: 787px; overflow: hidden; background: var(--page); }
  .canvas { position: relative; width: 1200px; height: 787px; }
  .sheet-frame {
    position: absolute; left: 123px; top: 0; width: 1077px; height: 786px;
    border: 1px solid var(--frame); border-top: none; border-right: none;
  }
  .label {
    position: absolute; top: 262px; width: 350px; height: 440px;
    background: linear-gradient(180deg, var(--label-top) 0%, var(--label-body) 45%, var(--label-bottom) 100%);
    overflow: hidden;
  }
  .label--left { left: 265px; }
  .label--right { left: 693px; }
  .brand-band {
    position: absolute; left: 0; top: 38px; width: 350px; height: 80px; background: var(--band-light);
  }
  .brand-mark {
    position: absolute; left: 140px; top: 8px; width: 60px; height: 60px; border-radius: 50%;
    background: radial-gradient(circle at 35% 30%, var(--gold-light), var(--gold) 55%, var(--gold-dark));
  }
  .brand-name {
    position: absolute; left: 0; top: 80px; width: 350px; text-align: center;
    font-family: "Questrial", sans-serif; font-size: 29px; color: var(--gold-text); white-space: nowrap;
  }
  .slogan {
    position: absolute; left: 0; top: 120px; width: 350px; text-align: center;
    font-family: "Great Vibes", cursive; font-size: 22px; line-height: 26px; color: var(--gold-dark);
  }
  .artwork {
    position: absolute; left: 18px; top: 152px; width: 74px; height: 158px;
    background: radial-gradient(ellipse at 50% 75%, #c89a45 0%, #e7c98a 45%, transparent 70%),
                linear-gradient(180deg, rgba(217,169,74,.45), rgba(217,169,74,.2) 50%, transparent 60%);
    border-radius: 40% 40% 50% 50%;
  }
  .product-title {
    position: absolute; left: 150px; top: 160px; width: 170px; text-align: center;
    font-family: "Cinzel", serif; font-weight: 700; font-size: 27px; letter-spacing: 3px; color: var(--ink);
  }
  .strength-pill {
    position: absolute; left: 143px; top: 198px; height: 30px; display: flex;
    border-radius: 15px; overflow: hidden; font-family: "Oswald", sans-serif; font-weight: 600; font-size: 18px; line-height: 30px;
  }
  .strength-pill .pill-name { padding: 0 4px 0 12px; color: var(--ink); background: linear-gradient(180deg, var(--silver), var(--silver-dark)); }
  .strength-pill .pill-dose { padding: 0 12px 0 4px; color: var(--ink); background: linear-gradient(180deg, var(--gold-light), var(--gold)); }
  .benefits { position: absolute; left: 138px; top: 250px; list-style: none; }
  .benefits li {
    display: flex; align-items: center; gap: 8px; height: 28px;
    font-family: "Roboto", sans-serif; font-weight: 700; font-size: 17px; color: var(--ink); white-space: nowrap;
  }
  .benefit-icon { width: 20px; height: 20px; flex: none; }
  .count-band {
    position: absolute; left: 0; top: 338px; width: 350px; height: 30px;
    background: linear-gradient(90deg, var(--gold-dark), var(--gold-light) 45%, var(--gold) 75%, var(--gold-dark));
  }
  .count-label {
    position: absolute; left: 112px; top: 338px; font-family: "Roboto", sans-serif; font-weight: 700;
    font-size: 21px; letter-spacing: 1px; color: var(--ink); line-height: 30px; white-space: nowrap;
  }
  .count-badge {
    position: absolute; left: 25px; top: 323px; width: 60px; height: 60px; border-radius: 50%;
    display: flex; align-items: center; justify-content: center;
    font-family: "Questrial", sans-serif; font-size: 32px;
  }
  .count-badge--cream { background: var(--cream); color: var(--gold-dark); border: 3px solid var(--gold); }
  .count-badge--gold {
    background: radial-gradient(circle, var(--gold-light) 0%, var(--gold) 60%, var(--gold-dark) 100%);
    color: var(--ink); border: 3px solid var(--gold-dark);
  }
  .cert-row { position: absolute; left: 134px; top: 380px; display: flex; gap: 7px; }
  .cert-badge { width: 28px; height: 28px; border-radius: 50%; background: var(--gold); border: 2px solid var(--gold-light); }
</style>
</head>
<body>
<div class="canvas">
  <div class="sheet-frame"></div>

  <section class="label label--left">
    <div class="brand-band"></div>
    <div class="brand-mark"></div>
    <div class="brand-name">Sun to Sun Vitamins</div>
    <div class="slogan">Rise Brighter!</div>
    <div class="artwork" role="img" aria-label="Golden tree growing from a heart, roots branching inside"></div>
    <div class="product-title">VITAMIN</div>
    <div class="strength-pill"><span class="pill-name">B-COMPLEX</span><span class="pill-dose">500MG</span></div>
    <ul class="benefits">
      <li><svg class="benefit-icon" viewBox="0 0 20 20"><circle cx="10" cy="10" r="10" fill="#d9a94a"/><path d="M11 3 6 11h4l-1 6 5-8h-4z" fill="#fff"/></svg>Energy Metabolism</li>
      <li><svg class="benefit-icon" viewBox="0 0 20 20"><circle cx="10" cy="10" r="10" fill="#d9a94a"/><path d="M3 10h4l1.5-3 2 6 1.5-3h5" fill="none" stroke="#fff" stroke-width="1.5"/></svg>Heart Health</li>
    </ul>
    <div class="count-band"></div>
    <div class="count-badge count-badge--cream">60</div>
    <div class="count-label">COATED CAPLETS</div>
    <div class="cert-row"><span class="cert-badge"></span><span class="cert-badge"></span><span class="cert-badge"></span><span class="cert-badge"></span></div>
  </section>

  <section class="label label--right">
    <div class="brand-band"></div>
    <div class="brand-mark"></div>
    <div class="brand-name">Sun to Sun Vitamins</div>
    <div class="slogan">Rise Brighter!</div>
    <div class="artwork" role="img" aria-label="Golden tree growing from a heart, roots branching inside"></div>
    <div class="product-title">VITAMIN</div>
    <div class="strength-pill"><span class="pill-name">B-COMPLEX</span><span class="pill-dose">500MG</span></div>
    <ul class="benefits">
      <li><svg class="benefit-icon" viewBox="0 0 20 20"><circle cx="10" cy="10" r="10" fill="#d9a94a"/><path d="M11 3 6 11h4l-1 6 5-8h-4z" fill="#fff"/></svg>Energy Metabolism</li>
      <li><svg class="benefit-icon" viewBox="0 0 20 20"><circle cx="10" cy="10" r="10" fill="#d9a94a"/><path d="M3 10h4l1.5-3 2 6 1.5-3h5" fill="none" stroke="#fff" stroke-width="1.5"/></svg>Heart Health</li>
    </ul>
    <div class="count-band"></div>
    <div class="count-badge count-badge--gold">60</div>
    <div class="count-label">COATED CAPLETS</div>
    <div class="cert-row"><span class="cert-badge"></span><span class="cert-badge"></span><span class="cert-badge"></span><span class="cert-badge"></span></div>
  </section>
</div>
</body>
</html>
```